Floral Waters needs a Label Design for bottles

Our products slogan: grown with water and sun.
Organic products of excellence originating from regions of extraordinary environmental quality, these products are the basis of natural cosmetics. Bio certificated and Organic.

We need a Luxury Label for the bottles of Floral Waters.
We don't want rustic, organic, rural, bio...
We want Luxury associated with environment.

The Label / decoration for the bottles must be editable, for we can change the titles of the floral Waters and information.
Elements :
Floral Water
Pet and Glass round Bottles Dimensions: 11cm Height , 4.5cm width
perimeter - 7.65
The logo is from tv lumora web store, it´s not necessary to include in the front of the paching design. it´s an open option

Target Market(s)

Medium High urban people , with ecologic and sustainable concerns. People who prefer natural and non Quimical cosmetics.

Industry/Entity Type

Floral

Requirements
Must have
• Sophisticated simple design
• Elements :
• Floral Water
• space for the name of the Floral Water ( ex: Salvia Officinalis, Minth, Melissa Officinalis)
• Grown with water and sun
Nice to have
• Variations of Gold
Should not have
• Bio, farm, organic, rustic,

```html
<!DOCTYPE html>
<html lang="en">
<head>
<meta charset="utf-8">
<title>Floral Water – Label Variations</title>
<link rel="stylesheet" href="https://fonts.googleapis.com/css2?family=Raleway:wght@400;500&family=Yellowtail&display=swap">
<style>
  :root {
    --backdrop: #efe9e0;
    --label-white: #f4f4f4;
    --ink: #2b2b2b;
    --script-green: #2f8a55;
    --band-black: #0c0c0c;
    --gold-light: #e4d49a;
    --gold-mid: #c2a95a;
    --gold-deep: #8f7a3a;
    --pattern-dark: #15130d;
  }
  * { box-sizing: border-box; margin: 0; padding: 0; }
  html, body { width: 1200px; height: 1169px; overflow: hidden; }
  body {
    background: var(--backdrop);
    position: relative;
    font-family: "Raleway", sans-serif;
  }
  .label-row {
    position: absolute;
    top: 230px;
    left: 75px;
    display: flex;
    gap: 75px;
  }
  .label {
    position: relative;
    width: 300px;
    height: 710px;
    background: linear-gradient(90deg, #e6e6e6 0%, var(--label-white) 20%, #ffffff 55%, #e9e9e9 100%);
    border-top: 6px solid var(--gold-mid);
    border-bottom: 6px solid var(--gold-mid);
    box-shadow: 0 10px 30px rgba(60, 45, 20, 0.18);
  }
  .ornament-band {
    position: absolute;
    left: 0;
    width: 100%;
    height: 118px;
    background:
      radial-gradient(circle at 30% 40%, rgba(200, 175, 100, 0.55), transparent 60%),
      radial-gradient(circle at 75% 65%, rgba(200, 175, 100, 0.45), transparent 55%),
      var(--pattern-dark);
  }
  .ornament-band.top { top: 0; }
  .ornament-band.bottom { bottom: 0; }
  .title {
    position: absolute;
    top: 166px;
    width: 100%;
    text-align: center;
    font-size: 21px;
    font-weight: 400;
    letter-spacing: 0.5px;
    color: var(--ink);
  }
  .slogan {
    position: absolute;
    top: 226px;
    width: 100%;
    text-align: center;
    font-family: "Yellowtail", cursive;
    font-size: 20px;
    line-height: 1.2;
    color: var(--script-green);
  }
  .name-band {
    position: absolute;
    left: 0;
    width: 100%;
    display: flex;
    align-items: center;
    justify-content: center;
    font-size: 20px;
    letter-spacing: 0.3px;
  }
  .rule {
    position: absolute;
    left: 0;
    width: 100%;
  }
  /* variation 1: black band */
  .v-black .name-band { top: 336px; height: 44px; background: var(--band-black); color: var(--gold-light); }
  .v-black .rule { height: 5px; background: var(--band-black); }
  .v-black .rule.above { top: 320px; }
  .v-black .rule.below { top: 390px; }
  /* variation 2: slim gold band */
  .v-gold-slim .name-band {
    top: 334px; height: 50px;
    background: linear-gradient(90deg, var(--gold-deep), var(--gold-light) 45%, var(--gold-mid) 75%, var(--gold-deep));
    color: var(--ink);
  }
  .v-gold-slim .rule { height: 4px; background: linear-gradient(90deg, var(--gold-deep), var(--gold-light), var(--gold-deep)); }
  .v-gold-slim .rule.above { top: 319px; }
  .v-gold-slim .rule.below { top: 395px; }
  /* variation 3: wide gold band */
  .v-gold-wide .name-band {
    top: 306px; height: 122px;
    background: linear-gradient(90deg, var(--gold-deep), var(--gold-light) 45%, var(--gold-mid) 75%, var(--gold-deep));
    color: var(--ink);
  }
  .volume {
    position: absolute;
    top: 550px;
    width: 100%;
    text-align: center;
    font-size: 10px;
    line-height: 12px;
    color: #555;
  }
</style>
</head>
<body>
  <main class="label-row">
    <section class="label v-black">
      <div class="ornament-band top" role="img" aria-label="Black and gold floral vine pattern"></div>
      <h1 class="title">FLORAL WATER</h1>
      <p class="slogan">Grown with water and sun</p>
      <div class="rule above"></div>
      <div class="name-band">SALVIA OFFICINALIS</div>
      <div class="rule below"></div>
      <p class="volume">400 ml 14.5 fl.oz</p>
      <div class="ornament-band bottom" role="img" aria-label="Black and gold floral vine pattern"></div>
    </section>
    <section class="label v-gold-slim">
      <div class="ornament-band top" role="img" aria-label="Black and gold floral vine pattern"></div>
      <h1 class="title">FLORAL WATER</h1>
      <p class="slogan">Grown with water and sun</p>
      <div class="rule above"></div>
      <div class="name-band">SALVIA OFFICINALIS</div>
      <div class="rule below"></div>
      <p class="volume">400 ml 14.5 fl.oz</p>
      <div class="ornament-band bottom" role="img" aria-label="Black and gold floral vine pattern"></div>
    </section>
    <section class="label v-gold-wide">
      <div class="ornament-band top" role="img" aria-label="Black and gold floral vine pattern"></div>
      <h1 class="title">FLORAL WATER</h1>
      <p class="slogan">Grown with water and sun</p>
      <div class="name-band">SALVIA OFFICINALIS</div>
      <p class="volume">400 ml 14.5 fl.oz</p>
      <div class="ornament-band bottom" role="img" aria-label="Black and gold floral vine pattern"></div>
    </section>
  </main>
</body>
</html>
```